WP website design (Vorne)

We need a wordpress design for an established auction and real estate company based in Kentucky. The winning design will incorporate a professional color scheme with company logo in a clean layout with specified widgets. The design needs to consider that this will be developed on a responsive theme. Colors will complement the colors in the logo.

Industry/Entity Type

Real Estate

Font styles to use
Sans Serif

Requirements
Must have
• - Navigation:
1) Home 2) Auctions 3) Real Estate Listings 4) Our Services 5) Why Auctions 6) About Us 7) Past Auctions 8) Contact Us

Homeage will have slideshow, please use stock real estate image as the initial slide. Homepage will have this content: "Martin Vorne Auctioneer Real Estate Broker

Buying or selling you can count on Martin Vorne Auctioneer to deliver a quality auction experience. We handle all the details from initial handshake to final payment. We are with you every step of the way giving our sellers the service and results they deserve. You only have one chance for a successful auction. Contact us today to see how our experience and know-how can work for you. We are confident that you will appreciate our higher standard of service."

Footer will have smaller company logo, and attached association logos and this contact info:
Phone: (270) 555-0148
Contacts: Martin Vorne
Email: martinvorne@mailbrook.example
Address: 482 Pellworth Lane • Bowling Green, KY 42917

Widgets:
1) email sign up 2) Social media (twitter, Youtube - can also be in header 3) News & Events Blog widget 4) testimonials blog 5) Featured Video widget
Nice to have
• Nice to Have:
- demonstrate the drop-down menu styling, e.g. under Auctions
-Upcoming Auctions
-Online Auctions
-Past Auctions

```html
<!DOCTYPE html>
<html lang="en">
<head>
<meta charset="utf-8">
<title>Martin Vorne Auctioneer Real Estate Broker</title>
<link href="https://fonts.googleapis.com/css2?family=Roboto:wght@300;400;500;700&family=Sorts+Mill+Goudy&display=swap" rel="stylesheet">
<style>
:root{
  --gold:#e6b412;
  --gold-dark:#c99a07;
  --gold-text:#c9980f;
  --blue:#2f7fd6;
  --blue-soft:#c9ddf3;
  --band:#e5e5e5;
  --text:#444;
  --muted:#666;
  --line:#cfcfcf;
  --white:#fff;
}
*{box-sizing:border-box;margin:0;padding:0}
html,body{width:946px;height:1200px;overflow:hidden;background:var(--white)}
body{font-family:"Roboto",Arial,sans-serif;color:var(--text);position:relative}
.abs{position:absolute}
.serif{font-family:"Sorts Mill Goudy",Georgia,serif;font-weight:400;color:#333}

/* header */
.brand{left:98px;top:30px;display:flex;align-items:center;gap:8px;font-size:22px;font-weight:700;color:var(--blue)}
.brand .mark{width:22px;height:22px;background:var(--gold)}
.contact-bar{right:102px;top:19px;display:flex;gap:12px;font-size:9px;color:#555;align-items:center}
.contact-bar span{display:flex;align-items:center;gap:5px}
.social{display:flex;gap:4px}
.social i{display:block;width:19px;height:19px;background:var(--blue)}
.social i.red{background:#d8262b}
.header-social{left:524px;top:61px}
.search{left:621px;top:54px;width:223px;height:27px;border:1px solid #ddd;background:#fafafa;font-size:8.5px;color:#999;padding:9px 8px}
.search .btn{position:absolute;right:-1px;top:-1px;width:31px;height:27px;background:var(--blue);display:flex;align-items:center;justify-content:center}

/* nav */
.nav{left:99px;top:96px;width:747px;height:30px;background:#f7f7f7;border-bottom:2px solid #ddd;display:flex;font-size:10.5px;color:#333;text-transform:uppercase}
.nav a{display:flex;align-items:center;padding:0 13px;text-decoration:none;color:inherit}
.nav a.active{background:var(--gold);color:var(--white);padding:0 18px}

.hero{left:99px;top:132px;width:747px;height:350px;border:4px solid var(--gold);
  background:linear-gradient(135deg,#c99a5a 0%,#e9cf98 40%,#f2de9c 60%,#e8d5a8 100%)}

/* welcome band */
.band{left:0;top:500px;width:946px;height:258px;background:var(--band)}
.welcome-title{left:94px;top:524px;font-size:33px}
.welcome-sub{left:99px;top:562px;font-size:12.5px;line-height:17px;color:var(--gold-text);font-weight:300}
.welcome-sub b{font-weight:700}
.welcome-body{left:97px;top:601px;width:280px;font-size:8.3px;line-height:14.6px;font-weight:300;color:#333}
.btn-gold{background:var(--gold);color:var(--white);font-size:9.5px;font-weight:300;display:flex;align-items:center;justify-content:center}
.read-more{left:94px;top:712px;width:67px;height:22px}
.vline{width:1px;background:var(--line)}
.hline{height:1px;background:var(--line)}
.tile{width:110px;text-align:center;font-size:9.5px;color:#555;font-weight:300}
.tile svg{display:block;margin:0 auto 8px}
.testi-title{left:676px;top:538px;font-size:12px;font-weight:500;color:#333;letter-spacing:.3px}
.bubble{left:670px;width:174px;height:36px;background:#f3f3f3;border-radius:5px;font-size:7.6px;line-height:10px;color:#777;padding:9px 10px;font-weight:300}
.bubble:after{content:"";position:absolute;left:18px;bottom:-6px;border:6px solid transparent;border-top-color:#f3f3f3;border-bottom:0;border-left:0}
.testi-name{left:672px;font-size:8.3px;color:#444}

/* news */
.section-title{font-size:32px;top:788px}
.news{width:222px;height:58px}
.date{position:absolute;left:0;top:0;width:45px;height:57px;border-radius:3px;overflow:hidden;box-shadow:0 1px 2px rgba(0,0,0,.2);color:var(--white);font-family:"Sorts Mill Goudy",Georgia,serif;text-align:center}
.date .d{height:35px;background:linear-gradient(#f7cd2f,#e2a90c);font-size:24px;line-height:36px}
.date .m{height:22px;background:var(--blue);font-size:16px;line-height:22px}
.news .txt{position:absolute;left:48px;top:0;width:174px;height:58px;background:#f1f1f1;border-radius:3px;font-size:7.6px;line-height:10px;color:#777;padding:9px 9px;font-weight:300}

/* sign up */
.signup{left:669px;top:851px;width:174px;height:139px;background:var(--blue-soft);border-radius:3px;font-size:8.3px;color:#555}
.signup .lbl{position:absolute;left:14px}
.signup .field{position:absolute;left:11px;width:153px;height:22px;background:var(--white);border-radius:3px}
.submit{position:absolute;left:13px;top:99px;width:52px;height:20px;border-radius:3px;background:linear-gradient(#f7cd2f,#e2a90c);color:var(--white);font-size:8.5px;display:flex;align-items:center;justify-content:center}

/* footer */
.footer{left:0;top:1032px;width:946px;height:168px;background:var(--band)}
.foot-brand{left:102px;top:1078px;display:flex;align-items:center;gap:5px;font-size:12px;font-weight:700;color:var(--blue)}
.foot-brand .mark{width:12px;height:12px;background:var(--gold)}
.copy{left:104px;top:1110px;width:150px;font-size:8px;line-height:10.5px;color:#666}
.foot-h{font-size:12.5px}
.foot-links{left:347px;top:1080px;font-size:8px;line-height:10px;color:#666;list-style:none}
.foot-contact{left:532px;font-size:7.6px;color:#555;display:flex;gap:8px;align-items:flex-start;line-height:9.5px}
</style>
</head>
<body>

<header>
  <div class="abs brand"><span class="mark"></span>Martin Vorne</div>
  <div class="abs contact-bar">
    <span><svg width="12" height="8" viewBox="0 0 12 8"><rect x=".5" y=".5" width="11" height="7" fill="#888"/><path d="M.5 .5 6 4.5 11.5 .5" stroke="#fff" fill="none"/></svg>martinvorne@mailbrook.example</span>
    <span><svg width="13" height="13" viewBox="0 0 13 13"><circle cx="6.5" cy="6.5" r="5.8" fill="none" stroke="#888"/><path d="M4.3 3.6c.5-.4 1-.3 1.2.2l.4 1c.1.4-.2.6-.4.8.3.8.9 1.4 1.6 1.7.2-.2.5-.5.9-.3l.9.5c.4.2.5.7.1 1.1-1.9 1.5-5.6-2.3-4.7-5z" fill="#888"/></svg>(270) 555-0148</span>
    <span><svg width="14" height="12" viewBox="0 0 14 12"><path d="M7 0 0 6h2v6h4V8h2v4h4V6h2z" fill="#888"/></svg>482 Pellworth Lane • Bowling Green, KY 42917</span>
  </div>
  <div class="abs social header-social"><i></i><i></i><i class="red"></i><i></i></div>
  <div class="abs search">Enter your search...
    <span class="btn"><svg width="16" height="16" viewBox="0 0 16 16"><circle cx="9.5" cy="6.5" r="4.7" fill="none" stroke="#fff" stroke-width="1.8"/><path d="M6 10 1.5 14.5" stroke="#fff" stroke-width="2.4" stroke-linecap="round"/></svg></span>
  </div>
  <nav class="abs nav">
    <a class="active">Home</a><a>Auctions</a><a>Real Estate Listings</a><a>Our Services</a><a>Why Auctions</a><a>About Us</a><a>Past Auctions</a><a>Contact Us</a>
  </nav>
</header>

<div class="abs hero" role="img" aria-label="Slideshow photo: house keys with a yellow auction tag beside reading glasses on a wooden desk"></div>

<section>
  <div class="abs band"></div>
  <h1 class="abs serif welcome-title">Welcome</h1>
  <p class="abs welcome-sub">Buying or selling you can<br>count on <b>Martin Vorne</b> Auctioneer</p>
  <p class="abs welcome-body">to deliver a quality auction experience. We handle all the details from initial handshake to final payment. We are with you every step of the way giving our sellers the service and results they deserve. You only have one chance for a successful auction. Contact us today to see how our experience and know-how can work for you. We are confident that you will appreciate our higher standard of service</p>
  <div class="abs btn-gold read-more">Read More</div>

  <div class="abs vline" style="left:396px;top:530px;height:152px"></div>
  <div class="abs vline" style="left:639px;top:530px;height:152px"></div>
  <div class="abs vline" style="left:518px;top:548px;height:140px"></div>
  <div class="abs hline" style="left:429px;top:613px;width:179px"></div>

  <div class="abs tile" style="left:407px;top:542px">
    <svg width="28" height="24" viewBox="0 0 28 24"><path d="M1 13 27 1 20 22 12 15 27 1M12 15v7l3-4" fill="none" stroke="#666" stroke-width="1.1" stroke-linejoin="round"/></svg>Under Auctions</div>
  <div class="abs tile" style="left:519px;top:542px">
    <svg width="30" height="32" viewBox="0 0 30 32"><circle cx="11" cy="10" r="8.5" fill="none" stroke="#666"/><circle cx="20" cy="22" r="8.5" fill="#e5e5e5" stroke="#666"/><circle cx="20" cy="22" r="6" fill="none" stroke="#666" stroke-width=".7"/><text x="11" y="14" font-size="10" text-anchor="middle" fill="#666" font-family="Arial">£</text><text x="20" y="26" font-size="9" text-anchor="middle" fill="#666" font-family="Arial">€</text></svg>Upcoming Auctions</div>
  <div class="abs tile" style="left:409px;top:628px">
    <svg width="30" height="24" viewBox="0 0 30 24"><rect x="1" y="1" width="28" height="17" fill="none" stroke="#666"/><path d="M1 15h28M11 23h8M15 18v5" stroke="#666"/></svg>Online Auctions</div>
  <div class="abs tile" style="left:509px;top:626px">
    <svg width="30" height="28" viewBox="0 0 30 28"><circle cx="15" cy="15" r="11" fill="none" stroke="#666"/><path d="M15 8v7l5 3M4 6l5-4M26 6l-5-4" fill="none" stroke="#666"/></svg>Past Auctions</div>

  <h2 class="abs testi-title">Testimonials</h2>
  <div class="abs bubble" style="top:575px">Lorem ipsum dolor sit amet, consectetur adipiscing elit. Integer a est vel quam</div>
  <div class="abs testi-name" style="top:622px">Owen Harlow</div>
  <div class="abs bubble" style="top:639px">Lorem ipsum dolor sit amet, consectetur adipiscing elit. Integer a est vel quam</div>
  <div class="abs testi-name" style="top:686px">Reid</div>
</section>

<section>
  <h2 class="abs serif section-title" style="left:98px">News &amp; Events</h2>
  <div class="abs news" style="left:103px;top:850px"><div class="date"><div class="d">23</div><div class="m">06</div></div><div class="txt">Lorem ipsum dolor sit amet, consectetur adipiscing elit. Integer a est vel quam dolor sit amet, consectetur adipiscing elit. Inte Integer a est vel quam d</div></div>
  <div class="abs news" style="left:381px;top:850px"><div class="date"><div class="d">23</div><div class="m">06</div></div><div class="txt">Lorem ipsum dolor sit amet, consectetur adipiscing elit. Integer a est vel quam dolor sit amet, consectetur adipiscing elit. Inte Integer a est vel quam d</div></div>
  <div class="abs news" style="left:103px;top:934px"><div class="date"><div class="d">23</div><div class="m">06</div></div><div class="txt">Lorem ipsum dolor sit amet, consectetur adipiscing elit. Integer a est vel quam dolor sit amet, consectetur adipiscing elit. Inte Integer a est vel quam d</div></div>
  <div class="abs news" style="left:381px;top:934px"><div class="date"><div class="d">23</div><div class="m">06</div></div><div class="txt">Lorem ipsum dolor sit amet, consectetur adipiscing elit. Integer a est vel quam dolor sit amet, consectetur adipiscing elit. Inte Integer a est vel quam d</div></div>

  <h2 class="abs serif section-title" style="left:666px">Sign up</h2>
  <form class="abs signup">
    <span class="lbl" style="top:11px">User Name</span>
    <span class="field" style="top:24px"></span>
    <span class="lbl" style="top:58px">Password</span>
    <span class="field" style="top:71px"></span>
    <span class="submit">Submit</span>
    <span class="lbl" style="left:97px;top:105px">New user Signin</span>
    <span class="lbl" style="top:124px">Forget password</span>
  </form>
</section>

<footer>
  <div class="abs footer"></div>
  <div class="abs foot-brand"><span class="mark"></span>Martin Vorne</div>
  <p class="abs copy">© 2014 &nbsp;|&nbsp; Privacy Policy &nbsp;All Rights Reserved</p>

  <h3 class="abs serif foot-h" style="left:347px;top:1061px">Links</h3>
  <ul class="abs foot-links">
    <li>Home</li><li>Auctions</li><li>Real Estate Listing</li><li>Our Services</li><li>Why Auctions</li><li>About Us</li><li>Past Auctions</li><li>Contact Us</li>
  </ul>

  <h3 class="abs serif foot-h" style="left:532px;top:1066px">Contact</h3>
  <div class="abs foot-contact" style="top:1091px"><svg width="12" height="8" viewBox="0 0 12 8"><rect x=".5" y=".5" width="11" height="7" fill="#888"/><path d="M.5 .5 6 4.5 11.5 .5" stroke="#fff" fill="none"/></svg>martinvorne@mailbrook.example</div>
  <div class="abs foot-contact" style="top:1112px"><svg width="13" height="13" viewBox="0 0 13 13"><circle cx="6.5" cy="6.5" r="5.8" fill="none" stroke="#888"/><path d="M4.3 3.6c.5-.4 1-.3 1.2.2l.4 1c.1.4-.2.6-.4.8.3.8.9 1.4 1.6 1.7.2-.2.5-.5.9-.3l.9.5c.4.2.5.7.1 1.1-1.9 1.5-5.6-2.3-4.7-5z" fill="#888"/></svg>(270) 555-0148</div>
  <div class="abs foot-contact" style="top:1138px"><svg width="14" height="12" viewBox="0 0 14 12"><path d="M7 0 0 6h2v6h4V8h2v4h4V6h2z" fill="#888"/></svg><span>482 Pellworth Lane •<br>Bowling Green, KY 42917</span></div>

  <h3 class="abs serif foot-h" style="left:758px;top:1062px">Social</h3>
  <div class="abs social" style="left:755px;top:1091px"><i></i><i></i><i class="red"></i><i></i></div>
</footer>

</body>
</html>
```